Local massage therapist needs some new marketing material

Hi there! I am a massage therapist here in Denver, CO in Brindle Hollow(shopping and art district) of the city. My business is called Lunora Massage of Denver. My practice has an eastern influence and I do reflexology, thai massage and use Chinese herbs, etc. I know all my clients and pay close attention to details. I am also very respectful of tradition and it shows in how I work. I tend to like modern, clean, fun, Asian designs. I am wanting a new business card and brochure. I have a logo and branding for my business that I want used in the design. Currently, the sign for my building is purple and I think my logo was designed to be purple. I will attach pictures of it and can send whatever files are necessary so it can be integrated into the brochure, etc. I like the purple but open to using other colors as well. Thanks!
My website is lunoramassagestudio.example where info can be gathered about me and services/fees for brochure.
Updates

Just increased budget. Please see new feedback in discussion thread.

Thanks!

                                       HEY ALL,

Just wanted to let you know that I made a change to my website. It is on the Prices Page. I no longer have the frequent  flyer prices but I added discounts. Let me know if you have any questions. Thanks so much!

Target Market(s)

healthy, urban, educated, upper middle class, yogis

Industry/Entity Type

Marketing

Requirements
Must have
• logo stays purple
Should not have
• not too busy

```html
<!DOCTYPE html>
<html lang="en">
<head>
<meta charset="utf-8">
<title>Lunora Massage of Denver – Brochure Inside Spread</title>
<link rel="stylesheet" href="https://fonts.googleapis.com/css2?family=Josefin+Sans:wght@300;400&family=Great+Vibes&family=Cormorant+SC:wght@500&display=swap">
<style>
  :root {
    --page-bg: #e6e5e1;
    --rose: #c44a85;
    --rose-deep: #a9296f;
    --plum: #8c1c76;
    --plum-dark: #6e135e;
    --sand: #ebe6d7;
    --taupe: #b0a482;
    --taupe-dark: #6f6650;
    --ink: #2c2a26;
    --white: #ffffff;
    --fold: rgba(0, 0, 0, 0.10);
  }
  * { box-sizing: border-box; margin: 0; padding: 0; }
  html, body { width: 1200px; height: 800px; overflow: hidden; }
  body { background: var(--page-bg); position: relative; font-family: "Josefin Sans", sans-serif; }

  .brochure {
    position: absolute; left: 96px; top: 40px; width: 1008px; height: 720px;
    overflow: hidden; background: var(--rose);
    box-shadow: 0 6px 24px rgba(0,0,0,0.18);
  }
  .panel { position: absolute; top: 0; width: 336px; height: 720px; }
  .panel--about { left: 0; }
  .panel--services { left: 336px; }
  .panel--extras { left: 672px; }

  /* imagery placeholders */
  .photo-hands {
    position: absolute; left: 0; top: 0; width: 1008px; height: 720px;
    background:
      radial-gradient(ellipse 260px 160px at 560px 90px, rgba(236,206,200,0.55), transparent 70%),
      radial-gradient(ellipse 300px 200px at 470px 380px, rgba(210,120,150,0.45), transparent 70%),
      linear-gradient(160deg, #cf5b92 0%, #c44a85 45%, #b33a7b 100%);
  }
  .photo-therapy-band {
    position: absolute; left: 0; top: 205px; width: 336px; height: 180px;
    background: linear-gradient(100deg, #c7b79a 0%, #a89a7a 50%, #d8ccb4 100%);
  }
  .portrait {
    position: absolute; left: 78px; top: 232px; width: 132px; height: 142px;
    background: linear-gradient(180deg, #8a93a8 0%, #6c7c99 60%, #2f6d8f 100%);
    border: 2px solid rgba(255,255,255,0.6);
    z-index: 3;
  }
  .photo-candle {
    position: absolute; left: 672px; top: 452px; width: 336px; height: 150px;
    background:
      radial-gradient(ellipse 70px 90px at 70px 90px, rgba(248,220,230,0.9), transparent 75%),
      linear-gradient(90deg, #d9a7bd 0%, #b58aa0 40%, #6f6650 100%);
  }

  .swoosh { position: absolute; left: 0; top: 0; width: 1008px; height: 720px; z-index: 2; }

  .fold { position: absolute; top: 0; width: 1px; height: 720px; background: var(--fold); z-index: 6; }
  .fold--one { left: 336px; }
  .fold--two { left: 672px; }

  /* brand */
  .brand {
    position: absolute; left: 0; top: 46px; width: 336px; text-align: center;
    color: var(--white); z-index: 4;
  }
  .brand__dot { width: 58px; height: 58px; border-radius: 50%; background: rgba(255,255,255,0.85); margin: 0 auto 22px; }
  .brand__name { font-weight: 300; font-size: 22px; letter-spacing: 2px; line-height: 1.3; }

  /* bio */
  .bio {
    position: absolute; left: 30px; top: 395px; width: 276px;
    font-family: "Cormorant SC", serif; font-weight: 500; font-size: 10.5px; line-height: 1.3;
    color: var(--ink); z-index: 4;
  }
  .bio p + p { margin-top: 7px; }
  .bio__name { font-size: 12.5px; }

  /* lists */
  .panel-title {
    position: absolute; left: 0; width: 336px; text-align: center;
    color: var(--white); font-weight: 300; z-index: 4;
  }
  .panel--services .panel-title { top: 62px; font-size: 36px; }
  .panel--extras .panel-title { top: 52px; font-size: 24px; line-height: 1.15; }

  .treatment-list {
    position: absolute; left: 0; width: 336px; list-style: none; text-align: center;
    font-family: "Great Vibes", cursive; color: var(--white);
    text-shadow: 0 1px 2px rgba(80,10,50,0.7); z-index: 4;
  }
  .panel--services .treatment-list { top: 140px; font-size: 33px; line-height: 1.05; }
  .panel--services .treatment-list li { margin-bottom: 16px; }
  .panel--extras .treatment-list { top: 135px; font-size: 33px; line-height: 1.1; }
  .panel--extras .treatment-list li { margin-bottom: 12px; }

  .quote-band {
    position: absolute; left: 672px; top: 602px; width: 336px; height: 118px;
    background: var(--plum); z-index: 3;
  }
  .quote {
    position: absolute; left: 20px; top: 14px; width: 296px; text-align: center;
    color: var(--white); font-size: 14px; line-height: 1.2; font-weight: 300;
  }
</style>
</head>
<body>
  <main class="brochure">
    <div class="photo-hands" role="img" aria-label="Photograph of a therapist's hands giving a back massage, tinted rose"></div>
    <div class="photo-therapy-band" role="img" aria-label="Photograph of a client relaxing during a massage, sepia toned"></div>
    <div class="photo-candle" role="img" aria-label="Photograph of a lit pillar candle and spa towels"></div>

    <svg class="swoosh" viewBox="0 0 1008 720" aria-hidden="true">
      <path d="M0 385 C 120 380, 260 420, 336 470 C 420 530, 520 590, 600 720 L 0 720 Z" fill="var(--sand)"/>
      <path d="M0 300 C 80 290, 200 330, 300 410 C 400 490, 520 560, 672 590 L 672 608 C 520 585, 390 520, 290 430 C 200 350, 90 318, 0 322 Z" fill="var(--plum)"/>
      <path d="M336 470 C 420 530, 520 590, 600 720 L 618 720 C 540 600, 440 528, 350 470 Z" fill="var(--taupe)"/>
      <path d="M600 720 C 640 680, 660 640, 672 602 L 672 720 Z" fill="var(--rose-deep)"/>
    </svg>

    <section class="panel panel--about">
      <div class="brand">
        <div class="brand__dot"></div>
        <div class="brand__name">Lunora Massage<br>of Denver</div>
      </div>
      <div class="portrait" role="img" aria-label="Portrait photograph of the therapist Mara Ellison"></div>
      <div class="bio">
        <p><span class="bio__name">Mara Ellison is</span> a registered massage therapist, a member of the Guild of Holistic Aromatherapy, Eastern Touch Alliance, Society of Massage Therapists, Bodywork Research Fund and League for Massage Education.</p>
        <p>She graduated from the Front Range Bodywork Institute and has formally studied Thai massage techniques at the Lanna Healing Arts School, Thailand. Presently, she is studying at Open Path Healers Academy with students from around the world to better understand natural health, energy work and spiritual counseling. Mara began meditation as a teen and learned the benefits of quieting the mind. Feeling the call within herself to help others, Mara naturally gravitated toward massage therapy and natural healing. Mara enjoys helping to facilitate people on their journeys toward health and personal happiness. She believes in an energy (chi) within us that when unobstructed, promotes our health and well being.</p>
        <p>She trusts in the body's natural capacity to heal, and takes advantage of this power in her delivery of bodywork.</p>
      </div>
    </section>

    <section class="panel panel--services">
      <h2 class="panel-title">Services</h2>
      <ul class="treatment-list">
        <li>Colorado Rain<br>(Seasonal Treatment)</li>
        <li>Swedish Escape</li>
        <li>Deep Tissue Therapy</li>
        <li>Table Thai Massage</li>
        <li>Blend Massage</li>
        <li>Prenatal Bliss</li>
      </ul>
    </section>

    <section class="panel panel--extras">
      <h2 class="panel-title">Extra Massage<br>Treats</h2>
      <ul class="treatment-list">
        <li>Chinese Fire Cupping</li>
        <li>Hot Stones</li>
        <li>Reflexology</li>
        <li>Thai Herbal Compress</li>
      </ul>
    </section>

    <div class="quote-band">
      <p class="quote">I invite you to take some time for yourself, for there truly is "more to life than increasing its speed".<br>– Anand Veer</p>
    </div>

    <div class="fold fold--one"></div>
    <div class="fold fold--two"></div>
  </main>
</body>
</html>
```